Push notification screens at app start up

We have an existing news publication app platform and are adding categories to push notifications.

We need two screens designed (each for Novaro, Tavlet and Morvelin for a total of 6d) that show when the app is first launched.

The workflow of our app:
0. app launch screen while webservices run (no work needed)
1. information screen to the user promoting the benefits of push notification with "Next" button. (see concept attached)
2. Push categories selection screen. This will have list of category types, with on/off switch.

"Select the categories that you wish to receive occasional notices:
Breaking News (on/off switch)
Local News (on/off switch)
Sports (on/off switch)
Local Events (on/off switch)
Weather Alerts (on/off switch)
Local Deals (on/off switch)"

"Enable these categories on the next screen."
"Next" button

Background:
When I was looking around at app designs, I came across this one (http://www.pixelvane.net/design/7148305) and I really liked it. We obviously have different features on our screen, but I’d like to have this same feel. The colors used in this design are perfect.

UPDATE: I do not mean to limit your design to match the layout as the one mentioned above. Please use your creativity for the layout.

Our standard font in Helvetica Neue.

Notes:
- our app is developed for all phone devices from Novaro 4 to Novaro 6, so designs should be thoughtful of vertical scrolling if needed.
- our app is developed for Tavlets, so we'll need designs completed as well. (We can finalize Novaro design first, then translate the design to Tavlet.)
- our app is developed for Morvelin phones (not tablets), so we'll need designs completed as well. (We can finalize Kvo design first, then translater to Morvelin UI design guidelines).

We hope to establish a good on-going relationship with the designer for as-needed work in the future.

Industry/Entity Type

News

Font styles to use
Other font styles liked:
• Helvetica Neue

Requirements
Must have
• Clean designs. No clutter.
Nice to have
• We would likely go with the standard on/off switches for both Kvo and Morvelin, but are open to small custom variations.

```html
<!DOCTYPE html>
<html lang="en">
<head>
<meta charset="utf-8">
<title>Notifications</title>
<link href="https://fonts.googleapis.com/css2?family=Inter:wght@400;500;600;700&display=swap" rel="stylesheet">
<style>
  :root {
    --brand-red: #f0141e;
    --ink-black: #000000;
    --surface: #ffffff;
    --label-grey: #5a5a5a;
    --icon-grey: #8c8c8c;
    --divider: #e2e2e2;
    --switch-off: #e5e5e5;
    --footnote-grey: #9a9a9a;
  }
  * { box-sizing: border-box; margin: 0; padding: 0; }
  html, body {
    width: 675px; height: 1200px; overflow: hidden;
    background: var(--ink-black);
    font-family: "Inter", "Helvetica Neue", Arial, sans-serif;
  }
  .screen { position: relative; width: 675px; height: 1200px; background: var(--ink-black); }

  .app-header { background: var(--brand-red); height: 140px; color: var(--surface); }
  .status-bar {
    height: 45px; display: flex; align-items: center; justify-content: space-between;
    padding: 0 14px; font-size: 22px; font-weight: 500;
  }
  .status-left, .status-right { display: flex; align-items: center; gap: 8px; width: 220px; }
  .status-right { justify-content: flex-end; }
  .status-time { font-weight: 600; }
  .signal { display: flex; gap: 3px; }
  .signal span { width: 11px; height: 11px; border-radius: 50%; border: 1.5px solid var(--surface); }
  .signal span.full { background: var(--surface); }

  .nav-bar { position: relative; height: 95px; display: flex; align-items: center; justify-content: center; }
  .nav-title { font-size: 35px; font-weight: 600; letter-spacing: 0.2px; }
  .back-button { position: absolute; left: 26px; top: 30px; }

  .header-gap { height: 45px; background: var(--ink-black); }

  .category-list { list-style: none; background: var(--surface); }
  .category-row {
    height: 99px; display: flex; align-items: center; position: relative;
    padding-left: 26px;
  }
  .category-row + .category-row::before {
    content: ""; position: absolute; top: 0; left: 0; right: 0; height: 2px; background: var(--divider);
  }
  .category-icon { width: 40px; height: 36px; flex: none; }
  .category-label {
    margin-left: 35px; font-size: 28px; font-weight: 600; color: var(--label-grey);
  }
  .switch {
    position: absolute; right: 12px; top: 24px;
    width: 90px; height: 52px; border-radius: 26px;
    background: var(--surface); box-shadow: inset 0 0 0 3px var(--switch-off);
  }
  .switch::after {
    content: ""; position: absolute; top: 2px; left: 2px;
    width: 48px; height: 48px; border-radius: 50%; background: var(--surface);
    box-shadow: 0 2px 5px rgba(0,0,0,0.3), 0 0 0 1px rgba(0,0,0,0.06);
  }
  .switch.is-on { background: var(--brand-red); box-shadow: none; }
  .switch.is-on::after { left: 40px; }

  .footnote {
    margin: 22px auto 0; width: 560px; text-align: center;
    color: var(--footnote-grey); font-size: 18.5px; line-height: 24px;
  }
</style>
</head>
<body>
<div class="screen">
  <header class="app-header">
    <div class="status-bar">
      <div class="status-left">
        <div class="signal"><span class="full"></span><span class="full"></span><span></span><span></span><span></span></div>
        <span>KESTREL</span>
        <svg width="24" height="18" viewBox="0 0 24 18" aria-hidden="true">
          <path d="M12 17 L2 6 A14 14 0 0 1 22 6 Z" fill="#fff"/>
        </svg>
      </div>
      <span class="status-time">4:21 PM</span>
      <div class="status-right">
        <svg width="14" height="22" viewBox="0 0 14 22" aria-hidden="true">
          <path d="M2 6 L12 15 L7 20 V2 L12 7 L2 16" fill="none" stroke="#fff" stroke-width="2"/>
        </svg>
        <span>100%</span>
        <svg width="44" height="20" viewBox="0 0 44 20" aria-hidden="true">
          <rect x="1" y="1" width="38" height="18" rx="4" fill="none" stroke="#fff" stroke-width="2"/>
          <rect x="4" y="4" width="32" height="12" rx="2" fill="#fff"/>
          <rect x="40" y="6" width="3" height="8" rx="1" fill="#fff"/>
        </svg>
      </div>
    </div>
    <nav class="nav-bar">
      <svg class="back-button" width="22" height="36" viewBox="0 0 22 36" aria-label="Back">
        <path d="M18 4 L5 18 L18 32" fill="none" stroke="#fff" stroke-width="5" stroke-linecap="round" stroke-linejoin="round"/>
      </svg>
      <h1 class="nav-title">Notifications</h1>
    </nav>
  </header>

  <div class="header-gap"></div>

  <ul class="category-list">
    <li class="category-row">
      <svg class="category-icon" viewBox="0 0 40 36" aria-hidden="true"><g fill="none" stroke="#8c8c8c" stroke-width="2"><rect x="1" y="1" width="38" height="34"/><rect x="6" y="8" width="11" height="10"/><path d="M21 9h13M21 13h13M21 17h13M6 23h28M6 28h28"/></g></svg>
      <span class="category-label">Breaking News</span>
      <span class="switch" role="switch" aria-checked="false"></span>
    </li>
    <li class="category-row">
      <svg class="category-icon" viewBox="0 0 40 36" aria-hidden="true"><g fill="none" stroke="#8c8c8c" stroke-width="2"><rect x="1" y="1" width="38" height="34"/><rect x="6" y="8" width="11" height="10"/><path d="M21 9h13M21 13h13M21 17h13M6 23h28M6 28h28"/></g></svg>
      <span class="category-label">Local News</span>
      <span class="switch is-on" role="switch" aria-checked="true"></span>
    </li>
    <li class="category-row">
      <svg class="category-icon" viewBox="0 0 40 36" aria-hidden="true"><g fill="none" stroke="#8c8c8c" stroke-width="2"><rect x="1" y="1" width="38" height="34"/><rect x="6" y="8" width="11" height="10"/><path d="M21 9h13M21 13h13M21 17h13M6 23h28M6 28h28"/></g></svg>
      <span class="category-label">Sports</span>
      <span class="switch" role="switch" aria-checked="false"></span>
    </li>
    <li class="category-row">
      <svg class="category-icon" viewBox="0 0 40 36" aria-hidden="true"><g fill="none" stroke="#8c8c8c" stroke-width="2"><rect x="1" y="1" width="38" height="34"/><rect x="6" y="8" width="11" height="10"/><path d="M21 9h13M21 13h13M21 17h13M6 23h28M6 28h28"/></g></svg>
      <span class="category-label">Local Events</span>
      <span class="switch" role="switch" aria-checked="false"></span>
    </li>
    <li class="category-row">
      <svg class="category-icon" viewBox="0 0 40 36" aria-hidden="true"><g fill="none" stroke="#8c8c8c" stroke-width="2"><rect x="1" y="1" width="38" height="34"/><rect x="6" y="8" width="11" height="10"/><path d="M21 9h13M21 13h13M21 17h13M6 23h28M6 28h28"/></g></svg>
      <span class="category-label">Weather Alerts</span>
      <span class="switch" role="switch" aria-checked="false"></span>
    </li>
    <li class="category-row">
      <svg class="category-icon" viewBox="0 0 40 36" aria-hidden="true"><g fill="none" stroke="#8c8c8c" stroke-width="2"><rect x="1" y="1" width="38" height="34"/><rect x="6" y="8" width="11" height="10"/><path d="M21 9h13M21 13h13M21 17h13M6 23h28M6 28h28"/></g></svg>
      <span class="category-label">Local Deals</span>
      <span class="switch" role="switch" aria-checked="false"></span>
    </li>
  </ul>

  <p class="footnote">Lorem Ipsum is simply dummy text of the printing and typesetting industry. Lorem Ipsum has been the industry's standard dummy text ever since the 1500s, when an unknown printer took a galley of type and scrambled it to make a type specimen book.</p>
</div>
</body>
</html>
```